Cultural Values, and Purpose, Vision and Mission statements design

We have recently created Cultural Values, and Purpose, Vision and Mission statements for a client’s business. We would like a visual representation created of each of these, to be hung on display in their office. For this project, we would like four (4) graphic design prints drawn up that depict:1. Purpose2. Vision3. Mission4. Cultural ValuesAll print designs should use a recurring, common theme, and be reflective of the business’ colours (see attached logo.)Please read and follow specifications in attached design brief.
Updates

Need extra days to review

Target Market(s)

Females, aged between 37 and 57 years old, who are family orientated, living locally, married and have between 1 and 3 children living at home.

Requirements
Must have
• Photoshop (PSD) format: All completed design will need to be in Photoshop (PSD) format before being handed over. This is to ensure that we can make alterations before printing if necessary.
• Quality: All designs must be 300 pixels resolution or higher.
• Purpose, Vision & Mission Designs Dimensions: The dimensions for each of the Purpose, Vision and Mission designs will need to be 30.5cm x 40.6cm (portrait, rectangle shape) with a surrounding 3.8cm border as it will be printed onto canvas matching these specifications.
• Cultural Values Dimensions: There are no specific dimensions required for the Cultural Values so the designer should feel free to display them best they see fit.
• Theme: All must follow the same theme and be reflective of the business's colours and logo.

```html
<!DOCTYPE html>
<html lang="en">
<head>
<meta charset="utf-8">
<title>Cultural Values</title>
<link rel="stylesheet" href="https://fonts.googleapis.com/css2?family=Bodoni+Moda:wght@500;600&family=Montserrat:wght@500;600&display=swap">
<style>
  :root {
    --backdrop: #e6e6e6;
    --sun-top: #fbb832;
    --sun-mid: #fcd52c;
    --sun-low: #fcb62c;
    --plum: #7b2773;
    --sky: #1fb0de;
    --sky-dark: #0d8fc0;
    --amber: #f9a11b;
    --orchid: #9b2f8f;
    --orchid-light: #b849a8;
    --leaf: #6cb33f;
    --leaf-dark: #4f9a2a;
    --pill-frame: #d4d2d0;
    --pill-face: #f7f7f6;
    --ink: #222222;
    --brand-grey: #8a8a8a;
    --brand-orange: #ef7d1a;
  }
  html, body {
    margin: 0;
    width: 1200px;
    height: 1200px;
    overflow: hidden;
    background: var(--backdrop);
  }
  .poster {
    position: absolute;
    left: 198px;
    top: 8px;
    width: 805px;
    height: 1184px;
    box-shadow: 0 6px 18px rgba(0,0,0,.18);
  }
  .poster svg { display: block; width: 100%; height: 100%; }
  .title { font-family: "Bodoni Moda", serif; font-weight: 600; fill: var(--plum); }
  .value-name { font-family: "Bodoni Moda", serif; font-weight: 500; font-size: 17px; letter-spacing: 1px; }
  .value-copy { font-family: "Montserrat", sans-serif; font-weight: 500; font-size: 11.4px; fill: var(--ink); letter-spacing: .2px; }
  .brand-name { font-family: "Montserrat", sans-serif; font-weight: 600; font-size: 40px; fill: var(--brand-orange); }
  .brand-tagline { font-family: "Montserrat", sans-serif; font-weight: 500; font-size: 14px; fill: #c9c9c9; letter-spacing: 3px; }
  .icon-line { fill: none; stroke: #1d1d1d; stroke-width: 1.6; stroke-linecap: round; stroke-linejoin: round; }
</style>
</head>
<body>
<div class="poster">
  <svg viewBox="0 0 805 1190" xmlns="http://www.w3.org/2000/svg">
    <defs>
      <linearGradient id="sun" x1="0" y1="0" x2="0" y2="1">
        <stop offset="0" stop-color="var(--sun-top)"/>
        <stop offset=".3" stop-color="var(--sun-mid)"/>
        <stop offset=".62" stop-color="var(--sun-low)"/>
        <stop offset=".78" stop-color="#fdd173"/>
        <stop offset=".83" stop-color="#ffffff"/>
        <stop offset="1" stop-color="#ffffff"/>
      </linearGradient>
      <filter id="soft" x="-10%" y="-20%" width="120%" height="140%">
        <feDropShadow dx="0" dy="4" stdDeviation="5" flood-opacity=".22"/>
      </filter>
    </defs>

    <rect class="poster-ground" width="805" height="1190" fill="url(#sun)"/>
    <path class="poster-ground-edge" fill="#ffffff" d="M0 930 L40 955 60 935 95 970 130 945 170 985 210 990 300 1000 420 985 560 990 640 945 680 900 700 930 730 890 760 910 805 880 L805 1190 0 1190Z"/>

    <text class="title" x="402" y="150" font-size="92" text-anchor="middle" letter-spacing="8">CULTURAL</text>
    <text class="title" x="402" y="278" font-size="134" text-anchor="middle" letter-spacing="2">VALUES</text>

    <g class="value value-pride" filter="url(#soft)">
      <path d="M620 355 L690 355 725 400 690 447 620 447Z" fill="var(--sky)"/>
      <circle cx="587" cy="402" r="78" fill="var(--sky-dark)"/>
      <rect x="215" y="338" width="420" height="127" rx="63" fill="var(--pill-frame)"/>
      <rect x="230" y="353" width="400" height="97" rx="48" fill="var(--pill-face)"/>
      <circle cx="587" cy="402" r="58" fill="#e6e6e6"/>
      <circle cx="587" cy="402" r="36" fill="var(--sky)"/>
      <g class="icon-line" transform="translate(587 402)">
        <path d="M0 -26 L20 -18 C20 4 12 18 0 26 C-12 18 -20 4 -20 -18Z"/>
        <path d="M0 -19 L14 -13 C14 2 8 12 0 18 C-8 12 -14 2 -14 -13Z"/>
        <path d="M0 -19 V18 M-14 -2 H14"/>
      </g>
    </g>
    <text class="value-name" x="246" y="375" fill="var(--sky-dark)">PRIDE</text>
    <text class="value-copy">
      <tspan x="245" y="396">We take pride in our workmanship, pride in</tspan>
      <tspan x="245" y="410.5">our service and pride in the knowledge that</tspan>
      <tspan x="245" y="425">we help to keep our clients safe, secure and</tspan>
      <tspan x="245" y="439.5">happy whilst they are on the road</tspan>
    </text>

    <g class="value value-honesty" filter="url(#soft)">
      <path d="M170 525 L100 525 65 570 100 615 170 615Z" fill="var(--amber)"/>
      <circle cx="205" cy="570" r="78" fill="var(--amber)"/>
      <rect x="145" y="507" width="435" height="128" rx="64" fill="var(--pill-frame)"/>
      <rect x="158" y="521" width="407" height="98" rx="49" fill="var(--pill-face)"/>
      <circle cx="205" cy="570" r="58" fill="#e6e6e6"/>
      <circle cx="205" cy="570" r="36" fill="var(--amber)"/>
      <g class="icon-line" transform="translate(205 570)">
        <path d="M0 -24 V20 M-10 22 H10 M-26 -15 H26"/>
        <path d="M-20 -15 L-30 5 H-10Z M20 -15 L10 5 H30Z"/>
      </g>
    </g>
    <text class="value-name" x="276" y="546" fill="var(--ink)">HONESTY</text>
    <text class="value-copy">
      <tspan x="277" y="568">We believe in providing an honest</tspan>
      <tspan x="277" y="582.5">service, honest advice, open and honest</tspan>
      <tspan x="277" y="597">communication and honest rates</tspan>
    </text>

    <g class="value value-respect" filter="url(#soft)">
      <path d="M680 708 L752 708 788 753 752 798 680 798Z" fill="var(--orchid-light)"/>
      <circle cx="645" cy="753" r="78" fill="var(--orchid)"/>
      <rect x="271" y="690" width="420" height="128" rx="64" fill="var(--pill-frame)"/>
      <rect x="286" y="704" width="400" height="98" rx="49" fill="var(--pill-face)"/>
      <circle cx="645" cy="753" r="58" fill="#e6e6e6"/>
      <circle cx="645" cy="753" r="36" fill="var(--orchid)"/>
      <g class="icon-line" transform="translate(645 753)">
        <path d="M-30 -10 L-20 -12 L-6 -2 L4 -8 L20 -12 L30 -10 M-30 8 L-22 6 L-6 14 Q0 16 4 12 L18 2"/>
        <path d="M-6 -2 L-12 4 Q-9 8 -4 5 L4 -1"/>
      </g>
    </g>
    <text class="value-name" x="299" y="729" fill="var(--plum)">RESPECT</text>
    <text class="value-copy">
      <tspan x="299" y="753">We uphold respect for our clients,</tspan>
      <tspan x="299" y="767.5">for their vehicles and for the automotive</tspan>
      <tspan x="299" y="782">industry in which we work</tspan>
    </text>

    <g class="value value-diligence" filter="url(#soft)">
      <path d="M205 875 L140 875 103 920 140 965 205 965Z" fill="var(--leaf)"/>
      <circle cx="241" cy="920" r="78" fill="var(--leaf)"/>
      <rect x="168" y="858" width="440" height="127" rx="63" fill="var(--pill-frame)"/>
      <rect x="180" y="872" width="412" height="97" rx="48" fill="var(--pill-face)"/>
      <circle cx="241" cy="920" r="58" fill="#e6e6e6"/>
      <circle cx="241" cy="920" r="36" fill="var(--leaf-dark)"/>
      <g class="icon-line" transform="translate(241 920)">
        <circle cx="-5" cy="-5" r="16"/>
        <path d="M7 7 L24 24 M-11 2 V-4 M-5 2 V-12 M1 2 V-7"/>
      </g>
    </g>
    <text class="value-name" x="316" y="897" fill="var(--leaf)">DILIGENCE</text>
    <text class="value-copy">
      <tspan x="316" y="916">We will work diligently to find and</tspan>
      <tspan x="316" y="930.5">communicate automotive solutions</tspan>
      <tspan x="316" y="945">that accommodate the individual</tspan>
      <tspan x="316" y="959.5">needs of our clients</tspan>
    </text>

    <g class="brand">
      <rect x="232" y="1070" width="32" height="32" fill="var(--brand-grey)"/>
      <text class="brand-name" x="280" y="1103">Ridgeway Auto</text>
      <text class="brand-tagline" x="282" y="1130">DRIVE WELL, ARRIVE HOME</text>
    </g>
  </svg>
</div>
</body>
</html>
```